ebook cover for a womens core fitness business

I need an ebook cover for an email capture gift. The title is "Ways to iron-clad your lower stability". My website provides online workouts for women focussing on their core and pelvic floor muscles. My business is "Lumen Motion with Tia" I have attached my color scheme as well as logo file

Target Market(s)

Females from child bearing age onwards

Industry/Entity Type

Health And Wellness

Font styles to use
Sans Serif

Colors
33a6d7
0455a3
cee9f5

Requirements
Must have
• Colours as per file.
• Feel fresh and attractive to women but not flowery
• Look professional
Should not have
• Flowers

```html
<!DOCTYPE html>
<html lang="en">
<head>
<meta charset="UTF-8">
<title>Ways to Iron-Clad Your Lower Stability — Lumen Motion with Tia</title>
<link rel="stylesheet" href="https://fonts.googleapis.com/css2?family=PT+Serif:wght@400;700&family=Lato:wght@300;400&display=swap">
<style>
  :root {
    --sky-deep: #3f7f9c;
    --sky-mid: #8fb7bf;
    --sun-glow: #f8f3c6;
    --haze: #e8e4b4;
    --horizon: #b9b99a;
    --road: #5a3a3e;
    --road-dark: #3b2a30;
    --ink: #111111;
    --brand-band: #2e8ee8;
    --brand-text: #ffffff;
    --page: #ffffff;
  }
  * { margin: 0; padding: 0; box-sizing: border-box; }
  html, body {
    width: 800px;
    height: 1200px;
    overflow: hidden;
    background: var(--page);
  }
  .cover {
    position: relative;
    width: 800px;
    height: 1200px;
    overflow: hidden;
  }
  .cover-photo {
    position: absolute;
    inset: 0;
    background:
      radial-gradient(circle at 575px 300px, var(--sun-glow) 0, rgba(248,243,198,0.85) 130px, rgba(232,228,180,0) 420px),
      linear-gradient(180deg, var(--sky-deep) 0%, var(--sky-mid) 22%, var(--haze) 55%, var(--horizon) 82%, var(--road) 86%, var(--road-dark) 100%);
  }
  .cover-photo::after {
    content: "";
    position: absolute;
    inset: 0;
    background: linear-gradient(90deg, rgba(40,70,90,0.35) 0%, rgba(40,70,90,0) 45%);
  }
  .title {
    position: absolute;
    right: 33px;
    top: 488px;
    text-align: right;
    color: var(--ink);
    line-height: 1;
  }
  .title-line { display: block; white-space: nowrap; }
  .title-lead {
    font-family: "PT Serif", Georgia, serif;
    font-weight: 400;
    font-size: 68px;
  }
  .title-feature {
    font-family: "Lato", Arial, sans-serif;
    font-weight: 300;
    font-size: 72px;
    margin-top: 6px;
    letter-spacing: -1px;
  }
  .title-link {
    font-family: "PT Serif", Georgia, serif;
    font-weight: 400;
    font-size: 52px;
    margin-top: 10px;
  }
  .title-key {
    font-family: "PT Serif", Georgia, serif;
    font-weight: 700;
    font-size: 74px;
    margin-top: 4px;
  }
  .brand-band {
    position: absolute;
    left: 0;
    right: 0;
    top: 1075px;
    height: 107px;
    background: var(--brand-band);
    display: flex;
    align-items: center;
    justify-content: center;
  }
  .brand-name {
    font-family: "Lato", Arial, sans-serif;
    font-weight: 400;
    font-size: 36px;
    color: var(--brand-text);
    letter-spacing: 0.5px;
  }
</style>
</head>
<body>
  <main class="cover">
    <div class="cover-photo" role="img" aria-label="Photo of a woman running along a coastal road, silhouetted against a bright low sun and hazy sky"></div>
    <h1 class="title">
      <span class="title-line title-lead">WAYS TO</span>
      <span class="title-line title-feature">IRON-CLAD</span>
      <span class="title-line title-link">YOUR LOWER</span>
      <span class="title-line title-key">STABILITY</span>
    </h1>
    <footer class="brand-band">
      <span class="brand-name">Lumen Motion with Tia</span>
    </footer>
  </main>
</body>
</html>
```